VoRUx marketing_clinical trial operations management

create a brochure template to include the content supplied, as well as general content such as logo, contact information and etc.

```html
<!DOCTYPE html>
<html lang="en">
<head>
<meta charset="utf-8">
<title>VoRUx Brochure Spread</title>
<link href="https://fonts.googleapis.com/css2?family=Oswald:wght@300;400&family=Arimo:wght@400;700&display=swap" rel="stylesheet">
<style>
:root{
  --blue-top:#1d5db4;
  --blue-mid:#1a55a8;
  --blue-deep:#173f8c;
  --band:#2f74cc;
  --band-dark:#1b4a9a;
  --spine:#0f2f6e;
  --white:#ffffff;
  --ink:#1a1a1a;
  --table-fill:#f4f0bf;
  --chart-blue:#2f6fd0;
  --chart-red:#c8413a;
}
*{margin:0;padding:0;box-sizing:border-box}
html,body{width:1200px;height:900px;overflow:hidden;background:#fff}
.spread{position:relative;width:1200px;height:900px;overflow:hidden;
  background:linear-gradient(180deg,var(--blue-top) 0%,var(--blue-mid) 45%,var(--blue-deep) 75%,var(--blue-mid) 100%);
  font-family:"Arimo",Arial,sans-serif;color:var(--white)}
.decor{position:absolute;inset:0}
.spine{position:absolute;left:599px;top:0;width:3px;height:900px;background:linear-gradient(90deg,var(--spine),rgba(15,47,110,.2))}
.block{position:absolute;font-size:10.3px;line-height:13.6px;letter-spacing:-.1px}
.block p{margin-bottom:13.6px}
.just{text-align:justify;font-size:10.1px;line-height:13.5px;letter-spacing:-.15px}
.page-title{position:absolute;font-family:"Oswald",sans-serif;font-weight:300;font-size:21px;letter-spacing:.1px;white-space:nowrap}
.big-heading{position:absolute;left:43px;top:318px;width:303px;font-size:21.5px;line-height:28px;font-weight:400;letter-spacing:-.2px}
.heading-line{display:flex;justify-content:space-between;white-space:nowrap}
.heading-line.last{justify-content:flex-start}
.list p{padding-left:7px;text-indent:-7px}
.list p.plain{padding-left:0;text-indent:0}
.photo{position:absolute;top:655px;height:245px}
.photo-left{left:0;width:599px;background:linear-gradient(135deg,#0b1e3a 0%,#24456f 40%,#6d8fb3 65%,#2a3f5e 100%)}
.photo-right{left:602px;width:598px;background:linear-gradient(160deg,#cfe3f6 0%,#5d8fc6 35%,#1c3f75 70%,#0d2245 100%)}
.table-wrap{position:absolute;left:625px;top:320px;width:272px;height:112px;background:var(--table-fill);overflow:hidden}
.table-caption{padding:2px 5px 1px;font-size:4.6px;line-height:5.5px;color:var(--ink);font-weight:700}
.data-table{width:100%;border-collapse:collapse;font-size:4.8px;line-height:5.6px;color:var(--ink)}
.data-table td{border:.5px solid #bdb88a;padding:1px 2px;text-align:center;vertical-align:top}
.data-table td.row-label{text-align:left;width:52px}
.chart{position:absolute;left:906px;top:151px;width:268px;height:171px;background:var(--white)}
</style>
</head>
<body>
<main class="spread">
  <svg class="decor" width="1200" height="900" aria-hidden="true">
    <polygon points="0,398 405,398 340,470 0,470" fill="var(--band)" opacity=".45"/>
    <polygon points="600,398 1200,398 1200,470 660,470" fill="var(--band)" opacity=".4"/>
    <polygon points="0,540 600,540 600,600 0,600" fill="var(--band-dark)" opacity=".35"/>
    <polygon points="600,510 1060,510 1120,570 600,570" fill="var(--band-dark)" opacity=".4"/>
    <polygon points="60,590 200,590 120,680 0,680 0,650" fill="var(--band)" opacity=".5"/>
    <polygon points="260,590 500,590 470,620 230,620" fill="var(--band)" opacity=".55"/>
    <polygon points="220,620 560,620 540,655 215,655" fill="var(--band-dark)" opacity=".5"/>
    <polygon points="720,590 960,590 990,620 750,620" fill="var(--band)" opacity=".55"/>
    <polygon points="1000,590 1200,590 1200,680 1080,680" fill="var(--band)" opacity=".5"/>
    <polygon points="600,0 660,0 640,40 600,40" fill="var(--band-dark)" opacity=".5"/>
    <polygon points="540,0 600,0 600,40 560,40" fill="var(--band-dark)" opacity=".5"/>
  </svg>
  <div class="spine"></div>

  <!-- Left page -->
  <h1 class="page-title" style="left:43px;top:69px">VoRUx Introduction</h1>
  <div class="block list" style="left:43px;top:109px;width:312px">
    <p class="plain">VoRUx is a data-driven solution provider serving clinical development organizations around the world in the following areas:</p>
    <p>- Select best investigator sites: proven to deliver superior enrollment results</p>
    <p>- Assess clinical trial feasibility: reliably identify the potential challenges for clinical trials in planning, and allow our clients to proactively take action to mitigate risk</p>
    <p>- process improvement support: quantify opportunities potentially can be improved, recommend actions to realize the opportunities, measure the impact from implementation, and reward the people who contributed to the achievement</p>
  </div>
  <h2 class="big-heading">
    <span class="heading-line"><span>VoRUx</span><span>differentiate</span><span>itself</span><span>from</span></span>
    <span class="heading-line last">competitors with the following:</span>
  </h2>
  <div class="block list" style="left:43px;top:387px;width:312px">
    <p>- A second to none database both in scale and in capturing the details and dynamic in clinical development around the world</p>
    <p>- A method with conceptual innovation and protected by patents and know-hows</p>
    <p>- Consistently superior and quantifiable results from VoRUx services</p>
    <p>- Continuing input from clients including the most prominent industry leaders</p>
    <p class="plain">VoRUx clients include Meridane, Pallexa, Sorvane, Novalith, Harlow &amp; Harlow, Biocrest Vale, Oteru, and many medium and smaller sized pharmaceutical/biopharmaceutical companies.</p>
  </div>
  <div class="photo photo-left" role="img" aria-label="Photo collage of business strategy icons and a hand touching a digital interface"></div>

  <!-- Right page -->
  <h1 class="page-title" style="left:630px;top:70px">VoRUx Site Selection Services</h1>
  <div class="block just" style="left:630px;top:114px;width:268px">
    Investigator site performance is one of the most important perennial challenges facing clinical trial execution teams across the industry. The inability to enroll the needed number of subjects in a targeted timeframe strains study budgets and resources, and prolongs cycle times.<br>
    VoRUx performance based site selection has been helping our clients to deliver superior enrollment results in more than 100 clinical trials, and the number of trials continues to grow rapidly.<br>
    Moreover, VoRUx recommended sites, as expected, have also resulted in decreased dropout, reduced query rate, and other improved quality measures.<br>
    The following table summarizes the results from a neuropathic pain clinical trial:
  </div>

  <div class="table-wrap">
    <div class="table-caption">Table 1 Measures Differentiating the Results Between the Sites Selected Based on Their Past Performance and the Sites Selected Based on Existing Method</div>
    <table class="data-table">
      <tr><td class="row-label"></td><td>Sites</td><td>Sites with Enrolled</td><td>Enrolled Patients</td><td>Enrolled Per Site</td><td>Completed Patients</td><td>Completed Per Site</td><td>Adjusted Queries</td><td>Queries Per Patient</td></tr>
      <tr><td class="row-label">Performance-Based Site Selection</td><td>15</td><td>12</td><td>81</td><td>5.4</td><td>55</td><td>3.7</td><td>4,001</td><td>73</td></tr>
      <tr><td class="row-label">Existing Site Selection</td><td>20</td><td>11</td><td>79</td><td>4.0</td><td>44</td><td>2.2</td><td>3,747</td><td>85</td></tr>
      <tr><td class="row-label">Overall Clinical Trial</td><td>35</td><td>23</td><td>160</td><td>4.6</td><td>99</td><td>2.8</td><td>7,748</td><td>78</td></tr>
      <tr><td class="row-label">Percentage Difference</td><td></td><td></td><td></td><td>35%</td><td></td><td>68%</td><td></td><td>16%</td></tr>
    </table>
  </div>

  <div class="block just" style="left:630px;top:455px;width:268px">
    VoRUx performance based site selection is enabled by an investigator performance database second to none in scale. This database is dynamic, and is updated automatically in real time. Our site selection services are also empowered by a combination of patent protected methods and technical know-how.<br>
    While VoRUx site selection is arguably the best in consistently delivering superior enrollment results, it is not a silver bullet.<br>
    &nbsp;As shown in the following chart, VoRUx site selection can
  </div>

  <div class="block just" style="left:907px;top:73px;width:268px">
    minimize non-performing sites (12% vs. 8%) and poor performing sites (12% vs. 7%), but we cannot eliminate them. On the other hand, while VoRUx site selection dramatically increases the top performing sites (9% vs. 28%), we cannot guarantee every site to be top performer:
  </div>

  <svg class="chart" viewBox="0 0 268 171" role="img" aria-label="Line chart of site performance distribution for seven T2DM trials">
    <text x="28" y="38" font-size="7.5" font-weight="700" fill="#222" font-family="Arimo, sans-serif">Site Performance Distribution for 7 T2DM Trials</text>
    <line x1="82" y1="64" x2="96" y2="64" stroke="var(--chart-blue)" stroke-width="2"/>
    <text x="99" y="66" font-size="4" fill="#444">Matched Sites</text>
    <line x1="130" y1="64" x2="144" y2="64" stroke="var(--chart-red)" stroke-width="2"/>
    <text x="147" y="66" font-size="4" fill="#444">Not Matched Sites</text>
    <line x1="10" y1="143" x2="262" y2="143" stroke="#ccc" stroke-width=".6"/>
    <polyline fill="none" stroke="var(--chart-blue)" stroke-width="1.8" points="28,111 66,118 104,110 142,104 180,94 218,110 256,12"/>
    <polyline fill="none" stroke="var(--chart-red)" stroke-width="1.8" points="28,89 66,91 104,102 142,103 180,98 218,109 256,107"/>
    <g font-size="5" fill="#222" font-family="Arimo, sans-serif">
      <text x="23" y="109">8%</text><text x="22" y="87">12%</text>
      <text x="62" y="126">7%</text><text x="60" y="88">12%</text>
      <text x="99" y="101">10%</text><text x="100" y="116">8%</text>
      <text x="137" y="101">9%</text><text x="143" y="101">9%</text>
      <text x="175" y="91">11%</text><text x="176" y="104">10%</text>
      <text x="213" y="106">9%</text><text x="213" y="114">8%</text>
      <text x="251" y="10">28%</text><text x="258" y="106">9%</text>
    </g>
    <g font-size="4.6" font-weight="700" fill="#222" font-family="Arimo, sans-serif" text-anchor="middle">
      <text x="28" y="158">NonEnroller</text><text x="66" y="158">Enrolled 1</text>
      <text x="104" y="158">Enrolled 2</text><text x="142" y="158">Enrolled 3</text>
      <text x="180" y="158">Enrolled 4</text><text x="218" y="158">Enrolled 5</text>
      <text x="250" y="158">Enrolled 13 or</text><text x="250" y="164">More</text>
    </g>
  </svg>

  <div class="block" style="left:907px;top:345px;width:270px">
    <p>This chart summarizes enrollment results from a set of seven type 2 diabetes clinical trials.</p>
    <p>We are proud of the fact that some of the drug candidates we have supported to develop are now available in the market, helping patients and saving lives.</p>
    <p>While we are happy to help our colleagues when their clinical trials are at planning stage, the reality is that we are often involved in "rescue missions", when a clinical trial needs more high performing sites to complete targeted enrollment.</p>
    <p>We are flexible in delivering our services. We can help our clients on providing site candidates one clinical trial at a time. Some other clients can access to our proprietary web based site selection tool, through a competitive annual fee.</p>
  </div>

  <div class="photo photo-right" role="img" aria-label="Photo of a businessman reaching toward a glowing digital world map interface"></div>
</main>
</body>
</html>
```